名刺のデザイン
弊社HPです。ご参考ください。

https://korinte72.example-site.jp/top

http://www.hoshizora-kitano.jp/
記載項目
GH brightpath
グループホーム ブライトパス

サービス管理責任者
小川 健
Takeru Ogawa
介護福祉士

株式会社rovanto.
〒433-8907 静岡県浜松市中区松風町418-135
携帯:070-4862-7153
TEL:053-478-3910
FAX:053-478-3915
E-mail:brightpath.kitano@mailbox-example.jp

<裏面>

経営理念
「ありがとう、あなたで良かった」
私たちと出会って良かったと言っていただけえるいただける
ことを目標にサービスを提供し続けます。

住宅型有料老人ホームホシゾラ北野
〒433-8907
静岡県浜松市中区松風町418-135
TEL:053-478-3910 FAX:053-478-3915
デイサービスこもれび北野の里
〒433-8907
静岡県浜松市中区松風町418-3096
TEL:053-478-3917 FAX:053-478-3915
(ロゴや施設写真を掲載する場合は添付データから切り出してください。)
希望イメージ
シンプル 複雑
単色 カラフル
暗い 明るい
日常 高級
遊び心 厳粛
未来的 伝統的
女性的 男性的
希望する色
水色系、緑系、黄・オレンジ系、ピンクなど可愛い色
補足説明
インクワークスなどに印刷を出すところまでお願いできると嬉しいです。

今回選ばせていただいた理由は弊社の運営コンセプト(雰囲気)を最も表現していただいていることです。

みなさま、今回は名刺デザインにご提案いただき、誠にありがとうございました。
これでけ多くのご提案をいただけたことをうれしく思います。
今後ともよろしくお願い申し上げます。

```html
<!DOCTYPE html>
<html lang="ja">
<head>
<meta charset="utf-8">
<title>名刺デザイン ブライトパス</title>
<link rel="stylesheet" href="https://fonts.googleapis.com/css2?family=M+PLUS+Rounded+1c:wght@400;700&family=Noto+Sans+JP:wght@400;700&display=swap">
<style>
:root{
  --page:#ffffff;
  --ink:#333333;
  --muted:#666666;
  --green:#5aa62e;
  --green-light:#cfe7a8;
  --orange:#ef8a1f;
  --cream:#fffbe3;
  --line:#9ccb6a;
}
*{margin:0;padding:0;box-sizing:border-box}
html,body{width:851px;height:1200px;overflow:hidden;background:var(--page)}
body{position:relative;font-family:"Noto Sans JP",sans-serif;color:var(--ink)}
.side-label{position:absolute;left:241px;font-size:10px;color:var(--muted)}
.card{position:absolute;left:241px;width:481px;height:283px;overflow:hidden;border:1px solid #e2e2e2}
.card--front{top:303px;background:#fff}
.card--back{top:688px;background:var(--cream)}
.abs{position:absolute}

/* front */
.brand{right:18px;top:18px;display:flex;align-items:center;gap:6px}
.brand__mark{width:26px;height:26px;border-radius:50%;background:var(--orange)}
.brand__name{font-family:"M PLUS Rounded 1c",sans-serif;font-weight:700;color:var(--green);font-size:12px;line-height:1.2}
.brand__name small{display:block;font-size:7px;font-weight:700}
.role{left:28px;top:80px;font-size:8px}
.person{left:28px;top:95px;display:flex;align-items:baseline;gap:10px}
.person__name{font-size:24px;font-weight:700;letter-spacing:.1em}
.person__roman{font-size:7px;color:var(--muted)}
.person-rule{left:28px;top:130px;width:200px;height:1px;background:var(--line)}
.company{left:28px;top:142px;font-size:8.5px;font-weight:700}
.contact{left:28px;top:158px;font-size:6.5px;line-height:1.65}
.foliage{right:0;bottom:0}

/* back */
.photos{left:18px;top:26px;display:flex;gap:4px}
.photo{width:46px;height:38px;background:linear-gradient(#b9c7cf,#8a7a62)}
.facility{left:18px;font-size:6.5px;line-height:1.55}
.facility__head{display:flex;align-items:center;gap:5px;margin-bottom:3px}
.facility__mark{width:18px;height:18px;border-radius:50%;background:var(--green)}
.facility__name{font-family:"M PLUS Rounded 1c",sans-serif;font-weight:700;color:var(--green);font-size:16px;line-height:1}
.facility__name small{display:block;font-size:6px;color:var(--ink);font-weight:400;margin-bottom:2px}
.philosophy{right:18px;top:22px;width:205px;padding:8px 10px;border:1px solid var(--orange);border-radius:4px;background:#fff;color:var(--orange);font-size:7.5px;line-height:1.8;text-align:center}
.plants{right:0;bottom:0}
</style>
</head>
<body>
<p class="side-label" style="top:283px">omote</p>
<section class="card card--front" aria-label="名刺 表面">
  <div class="abs brand"><span class="brand__mark"></span><p class="brand__name">GH brightpath<small>グループホーム ブライトパス</small></p></div>
  <p class="abs role">サービス管理責任者　介護福祉士</p>
  <div class="abs person"><h1 class="person__name">小川 健</h1><span class="person__roman">Takeru Ogawa</span></div>
  <div class="abs person-rule"></div>
  <p class="abs company">株式会社rovanto.</p>
  <p class="abs contact">〒433-8907 静岡県浜松市中区松風町418-135<br>携帯：070-4862-7153<br>TEL：053-478-3910　FAX：053-478-3915<br>E-mail：brightpath.kitano@mailbox-example.jp</p>
  <svg class="abs foliage" width="260" height="200" viewBox="0 0 260 200" role="img" aria-label="緑と黄色の葉や花のイラスト">
    <defs><radialGradient id="leafGlow" cx="70%" cy="70%" r="75%"><stop offset="0" stop-color="#8fc24f"/><stop offset=".6" stop-color="#cfe7a8"/><stop offset="1" stop-color="#ffffff" stop-opacity="0"/></radialGradient></defs>
    <path d="M260 0 C200 40 120 70 70 130 C40 165 0 185 0 200 L260 200 Z" fill="url(#leafGlow)"/>
  </svg>
</section>

<p class="side-label" style="top:671px">ura</p>
<section class="card card--back" aria-label="名刺 裏面">
  <div class="abs photos"><div class="photo" role="img" aria-label="施設外観写真"></div><div class="photo" role="img" aria-label="施設外観写真"></div></div>
  <div class="abs facility" style="top:80px">
    <div class="facility__head"><span class="facility__mark"></span><p class="facility__name"><small>住宅型有料老人ホーム</small>ホシゾラ北野</p></div>
    〒433-8907 静岡県浜松市中区松風町418-135<br>TEL：053-478-3910　FAX：053-478-3915
  </div>
  <div class="abs facility" style="top:160px">
    <div class="facility__head"><span class="facility__mark" style="background:var(--orange)"></span><p class="facility__name"><small>デイサービス</small>こもれび北野の里</p></div>
    〒433-8907 静岡県浜松市中区松風町418-3096<br>TEL：053-478-3917　FAX：053-478-3915
  </div>
  <p class="abs philosophy">「ありがとう、あなたで良かった」<br>私たちと出会って良かったと言って<br>いただけることを目標に<br>サービスを提供し続けます。</p>
  <svg class="abs plants" width="190" height="180" viewBox="0 0 190 180" role="img" aria-label="草花と葉のイラスト">
    <defs><linearGradient id="plantTone" x1="0" y1="0" x2="0" y2="1"><stop offset="0" stop-color="#cfe7a8" stop-opacity="0"/><stop offset=".5" stop-color="#a9d46f" stop-opacity=".7"/><stop offset="1" stop-color="#6fae3a"/></linearGradient></defs>
    <path d="M20 180 C30 110 80 60 150 20 C170 60 190 90 190 180 Z" fill="url(#plantTone)"/>
  </svg>
</section>
</body>
</html>
```